Holiday Rental Company Flyer Design (DL not A5)

Note from PixelFolk Administration: The category sizing selected is A5, however the project requires DL sized artwork. Please refer to the DL template link below while the 'Special Requirements' are updated accordingly.

Project Brief:
We need a double sided DL flyer designed for an up market Holiday Rental Company that portrays a personalised approach to property management. These are to be used for letter box drops to homes we're specifically targeting so the design should be modern, complimentary colour palette, uncluttered & visually appealing.

Please Download the DL Template from Quillmark here: http://www.quillmark.com.au/qm/ns/propath/UploadResources.aspx?selectedTab=0?pfid=BFB&pf_id=BFB&xnav=easypath-upload-image#Templates

Target Market(s)

Wealthy Home Owners

Industry/Entity Type

It Company

Font styles to use
Other font styles liked:
• Avant Garde Extra Light & Demi

Colors
33b8a4

Requirements
Must have
• DL Flyer sizes (210mm width x 99mm width, plus 3mm bleed)
• Front: Logo, Main Image & Grab
• Back: Contact Details & Brief Description of our business
• Images: Ideally the main image should be the house with the pool but alternatively a lifestyle images could also be used.
Nice to have
• A creative designer!
Should not have
• Clutter & busy designs

```html
<!DOCTYPE html>
<html lang="en">
<head>
<meta charset="utf-8">
<title>Harbourline Stays – DL Flyer</title>
<link rel="stylesheet" href="https://fonts.googleapis.com/css2?family=Poppins:wght@200;300;600&family=Open+Sans:wght@400;600;700&display=swap">
<style>
  :root {
    --stage: #7e8b88;
    --navy: #1d1a45;
    --violet: #5a46a8;
    --amber: #d9a94e;
    --teal: #33b8a4;
    --teal-soft: #8fd2c4;
    --sky: #c9dde4;
    --sea: #7fc3c9;
    --white: #ffffff;
    --ink: #2f3a3d;
  }
  * { box-sizing: border-box; margin: 0; padding: 0; }
  html, body { width: 1200px; height: 1148px; overflow: hidden; }
  body { background: var(--stage); position: relative; font-family: "Open Sans", sans-serif; }

  .flyer { position: absolute; left: 100px; width: 1000px; height: 472px; overflow: hidden; box-shadow: 0 6px 18px rgba(0,0,0,.25); }
  .flyer--front { top: 70px; }
  .flyer--back { top: 606px; }

  .photo { position: absolute; inset: 0; }
  .photo--house {
    background:
      linear-gradient(115deg, rgba(225,170,80,.85) 0%, rgba(150,100,90,.6) 28%, rgba(60,45,110,.2) 45%, transparent 60%),
      linear-gradient(160deg, #2a2560 0%, var(--navy) 40%, var(--violet) 80%, #8a78c8 100%);
  }
  .photo--sea {
    background: linear-gradient(180deg, #aac9d6 0%, var(--sky) 35%, #d6e7e8 55%, var(--sea) 62%, #5fb2b8 100%);
  }

  .brand { position: absolute; left: 225px; top: 48px; color: var(--white); font-family: "Poppins", sans-serif; font-weight: 200; font-size: 72px; line-height: 1; letter-spacing: 10px; }
  .brand__line { display: block; }
  .brand__line + .brand__line { margin-top: 6px; }
  .brand-mark { position: absolute; left: 438px; top: 236px; width: 64px; height: 64px; }

  .tagline-band { position: absolute; left: 0; right: 0; top: 372px; height: 54px; background: var(--navy); display: flex; align-items: center; padding-left: 190px; }
  .tagline { color: var(--white); font-family: "Poppins", sans-serif; font-weight: 200; font-size: 25px; letter-spacing: .5px; }

  .back-content { position: absolute; left: 68px; top: 40px; color: var(--white); width: 560px; }
  .headline { font-family: "Poppins", sans-serif; font-weight: 200; font-size: 42px; line-height: 1.1; margin-bottom: 18px; }
  .intro, .service-list li { font-size: 14px; line-height: 1.45; }
  .service-lead { font-size: 14px; font-weight: 700; line-height: 1.45; margin: 20px 0 8px; }
  .service-list { list-style: none; }
  .service-list li { display: flex; align-items: center; gap: 10px; margin-bottom: 8px; }
  .service-list svg { flex: none; }

  .cta-band { position: absolute; left: 0; right: 0; top: 345px; height: 38px; background: var(--teal-soft); display: flex; align-items: center; padding-left: 48px; color: var(--white); font-family: "Poppins", sans-serif; font-weight: 600; font-size: 16px; }
  .contact-strip { position: absolute; left: 0; right: 0; top: 383px; height: 38px; background: var(--white); display: flex; align-items: center; justify-content: space-between; padding: 0 48px; color: var(--teal); font-size: 14px; }
  .postal { position: absolute; left: 0; right: 0; top: 432px; text-align: center; color: var(--ink); font-size: 14px; }
</style>
</head>
<body>

<section class="flyer flyer--front" aria-label="Flyer front">
  <div class="photo photo--house" role="img" aria-label="Luxury holiday home at dusk with lit windows and a pool"></div>
  <h1 class="brand">
    <span class="brand__line">HARBOURLINE</span>
    <span class="brand__line">STAYS</span>
  </h1>
  <svg class="brand-mark" viewBox="0 0 64 64" aria-hidden="true">
    <circle cx="32" cy="32" r="28" fill="none" stroke="#ffffff" stroke-width="1.5"/>
  </svg>
  <div class="tagline-band">
    <p class="tagline">Holiday Rental Management with a difference</p>
  </div>
</section>

<section class="flyer flyer--back" aria-label="Flyer back">
  <div class="photo photo--sea" role="img" aria-label="Calm bay with a small moored sailing boat under a soft sky"></div>
  <div class="back-content">
    <h2 class="headline">What we do differently!</h2>
    <p class="intro">Rather than relying upon a key safe or a central pick-up destination,<br>a ‘Harbourline Stays’ staff member will greet guests upon arrival.</p>
    <p class="service-lead">Our ‘Meet &amp; Greet’ service provides home owners with<br>an increased level of Security and also allows us to:</p>
    <ul class="service-list">
      <li><svg width="16" height="16" viewBox="0 0 16 16" aria-hidden="true"><circle cx="8" cy="8" r="6" fill="none" stroke="#ffffff" stroke-width="1.2"/></svg>Prepare the home for their arrival (lights, heaters, music etc.)</li>
      <li><svg width="16" height="16" viewBox="0 0 16 16" aria-hidden="true"><circle cx="8" cy="8" r="6" fill="none" stroke="#ffffff" stroke-width="1.2"/></svg>Establish a rapport &amp; help facilitate future bookings</li>
      <li><svg width="16" height="16" viewBox="0 0 16 16" aria-hidden="true"><circle cx="8" cy="8" r="6" fill="none" stroke="#ffffff" stroke-width="1.2"/></svg>Reiterate their responsibilities to ensure the return of their bond</li>
    </ul>
  </div>
  <div class="cta-band">If you’d like to know what your property could achieve or require additional information, please contact us on:</div>
  <div class="contact-strip">
    <span>t: (03)5900 1234</span>
    <span>e: stay@harbourlinestays.com.au</span>
    <span>w: harbourlinestays.com.au</span>
  </div>
  <p class="postal">PO Box 12, Seaview Victoria 3900</p>
</section>

</body>
</html>
```